Simple website design to introduce our software product.

Hello there! If you please, we want a lot of images (attached) to have this site to have our prospects thinking about how great it will be to use this product in their facility/clinic/office. There are a lot of happy people in the images attached and this is the feeling we want to convey...with a modern technology edge since our product digitizes the patient survey process and is used on a tablet PC.

We are finalizing a name change of our product, it is currently called "QVRN" but we are considering coming up with a better name so in the interim we will use QVRN as a place holder. The website domain where this site will reside is www.themorrowtally.example

1. We would like large scrolling images SIMILAR TO the top portion of this website : http://lanternwickstudio.example/
Here are the verbiage blurbs to accompany the scrolling images:
Welcome to the next generation of Patient Experience Data Collection and Reporting. Presenting QVRN.

QVRN captures patient, nurse, doctor, employee and visitor satisfaction information in real time quickly and easily on a tablet PC.

QVRN gives you instantaneous benchmarking and reporting data including comparison reports, return rates, percentile rankings, positive and negative trending and much more.

QVRN DRAMATICALLY increases survey return rates.

QVRN empowers you to improve patient care when the data is relevant: NOW.

2. Please add something like the attached form called "QVRN info for pricing form" that says, "You won't believe our pricing! Click here" that includes the required fields as in the attached example.

3. We also want to highlight our Fernlattice Stewardship Accord so please include the verbiage (from our company website): https://www.qvrnltd.example/green.cfm I can provide you with the script to add the seal at the bottom left of the page.

4. We will provide verbiage for the About Us page and the Contact Us page

5. We would like to embed a video into the site and I can email you that code.

6. Please add the attached PLATINUM Fernlattice Stewardship Accord logo on all pages and link it to this: http://www.fernlattice.example/members/showseal/XyZ4Mw==/QmFzZWxpbmU=/

Looking forward to seeing what you present! Thank you for your entries. : )

We are very happy after seeing your designs.  Thank you so much.  Our product will be named The Morrow Tally, please update any and all instances of "QVRN" accordingly.  

Please be creative about this - How can an image of the tablet pc be used to navigate the site or maybe a specific section of the site?  

We have the domain www.themorrowtally.example and it is currently on a Weebly platform.  Could you/your team also launch our design on Weebly/Wordpress for us?

Hello!  Please be sure that the verbiage on your page designs is NOT pulled from our company website, QVRNovation (qvrnltd.example).  This is our PRODUCT website, not our COMPANY website.

Please make the site design concise.  Please include the following elements:  

1.  All designs must have a box (similar to file number 10 that is attached to the brief)
The title of the box needs to be "You won't believe our pricing!"
and has the following required fields:

*first name
*last name
*email
*phone
*company 
The submit button should say "GET IT!"  The position of this box should be on the right side of the page and while we want site visitors to see this box, we don't want it to be the first thing that draws their eye.  In other words, place this box softly/subtly on the site.  

2.  We like the images of the tablet pc.  It is very important that the site include pictures of PATIENTS with the tablet pc in their hands.  For this software, images of patients holding the tablet are more in alignment with the image we're trying to brand than are images of doctors/nurses holding the tablet pc. 

3.  Please update all designs to have the lead header/verbiage say "Welcome to the next generation of Patient Experience Data Collection and Reporting.  Presenting The Morrow Tally."  

4.  Please add this to the design too (if it's not already in your design), "Collect patient, doctor, nurse, employee and visitor Satisfaction/Experience feedback quickly, easily and in REAL TIME on a tablet pc."   

Please include this verbiage on the website - Users of The Morrow Tally consistently enjoy a survey return rate ABOVE 90%!

Target Market(s)

Healthcare facilities/hospitals/clinics/doctor's offices (initially, but the product can be customized for any industry).

Industry/Entity Type

Software

```html
<!DOCTYPE html>
<html lang="en">
<head>
<meta charset="utf-8">
<title>The Morrow Tally – Patient Experience Data Collection &amp; Reporting</title>
<link rel="stylesheet" href="https://fonts.googleapis.com/css2?family=Yanone+Kaffeesatz:wght@300;400;600;700&family=Raleway:wght@300;400&family=Open+Sans:wght@400;700&display=swap">
<style>
  :root {
    --brand-blue: #2b96c0;
    --brand-blue-text: #2a93bf;
    --hero-tint: #dff0f6;
    --leaf-green: #9bca3c;
    --ink: #3a3a3a;
    --ink-soft: #555;
    --paper: #ffffff;
    --form-panel: #f2f2f2;
    --field-border: #c9c9c9;
    --rule: #e6e6e6;
    --seal-fill: #e4f1f6;
  }
  * { box-sizing: border-box; margin: 0; padding: 0; }
  html, body { width: 981px; height: 1200px; overflow: hidden; }
  body { position: relative; background: var(--paper); font-family: "Open Sans", Arial, sans-serif; color: var(--ink); }
  a { color: inherit; text-decoration: none; }

  .top-band { position: absolute; left: 0; top: 0; width: 981px; height: 282px; background: var(--brand-blue); }

  .brand-dot { position: absolute; left: 40px; top: 37px; width: 46px; height: 46px; border-radius: 50%; background: var(--paper); }
  .brand-name { position: absolute; left: 142px; top: 27px; font-family: "Yanone Kaffeesatz", sans-serif; font-weight: 700; font-size: 54px; line-height: 46px; letter-spacing: .3px; color: var(--paper); white-space: nowrap; }
  .brand-tagline { position: absolute; left: 146px; top: 72px; font-family: "Yanone Kaffeesatz", sans-serif; font-weight: 400; font-size: 17px; letter-spacing: 1.2px; line-height: 18px; color: var(--paper); white-space: nowrap; }

  .main-nav { position: absolute; right: 28px; top: 78px; display: flex; gap: 26px; font-family: "Yanone Kaffeesatz", sans-serif; font-weight: 400; font-size: 20px; letter-spacing: .3px; color: var(--paper); }

  .hero { position: absolute; left: 22px; top: 114px; width: 935px; height: 293px; background: var(--hero-tint); }
  .slide-dots { position: absolute; right: 27px; top: 9px; display: flex; gap: 5px; }
  .slide-dots span { width: 10px; height: 10px; background: var(--brand-blue); }
  .slide-dots span.is-active { background: var(--leaf-green); }
  .hero-device { position: absolute; left: 8px; top: 66px; width: 460px; height: 285px; border-radius: 18px;
    background: linear-gradient(160deg, #3b3b3b 0%, #1e1e1e 55%, #9a9a9a 100%); }
  .hero-text { position: absolute; left: 482px; top: 92px; width: 445px; font-family: "Raleway", sans-serif; font-weight: 300; font-size: 25.5px; line-height: 30px; letter-spacing: -.2px; color: var(--brand-blue-text); }

  .features { position: absolute; left: 0; top: 486px; width: 981px; }
  .feature { position: absolute; top: 0; width: 280px; }
  .feature-icon { width: 64px; height: 64px; border-radius: 10px; background: var(--leaf-green); display: flex; align-items: center; justify-content: center; }
  .feature-title { font-family: "Raleway", sans-serif; font-weight: 300; font-size: 20px; letter-spacing: -.3px; color: var(--ink); margin-top: 18px; white-space: nowrap; }
  .feature-text { width: 250px; font-size: 12px; line-height: 14px; color: var(--ink-soft); margin-top: 12px; }
  .feature-more { display: block; font-size: 12px; color: #222; margin-top: 14px; }

  .divider { position: absolute; left: 65px; top: 683px; width: 838px; height: 1px; background: var(--rule); }

  .video { position: absolute; left: 61px; top: 711px; width: 326px; height: 271px; background: #000; }
  .video-frame { position: absolute; left: 0; top: 44px; width: 326px; height: 185px;
    background: linear-gradient(180deg, #cfe3ee 0%, #e8eef2 45%, #f4f6f7 100%); }
  .video-actions { position: absolute; right: 7px; top: 8px; display: flex; flex-direction: column; gap: 5px; }
  .video-actions span { width: 26px; height: 26px; background: #222; border-radius: 3px; display: flex; align-items: center; justify-content: center; }
  .video-controls { position: absolute; left: 8px; bottom: 8px; width: 310px; height: 28px; background: #1b1b1b; display: flex; align-items: center; gap: 8px; padding: 0 8px; }
  .video-track { flex: 1; height: 8px; background: #3a3a3a; border: 1px solid #555; position: relative; }
  .video-track::before { content: ""; position: absolute; left: 0; top: 0; width: 4px; height: 100%; background: var(--brand-blue); }

  .pricing { position: absolute; left: 448px; top: 713px; width: 459px; height: 269px; background: var(--form-panel); }
  .pricing-title { margin-top: 8px; text-align: center; font-family: "Yanone Kaffeesatz", sans-serif; font-weight: 700; font-size: 42px; color: var(--brand-blue-text); letter-spacing: .2px; white-space: nowrap; }
  .pricing-field { position: absolute; left: 83px; width: 276px; height: 26px; background: var(--paper); border: 1px solid var(--field-border); font-size: 12px; color: #555; padding: 4px 9px; }
  .pricing-field::after { content: "*"; position: absolute; left: 284px; top: 0; color: #444; font-size: 13px; }
  .pricing-submit { position: absolute; left: 83px; top: 197px; width: 276px; height: 52px; background: var(--leaf-green); color: var(--paper); font-weight: 700; font-size: 28px; letter-spacing: 1px; display: flex; align-items: center; justify-content: center; }

  .site-footer { position: absolute; left: 0; top: 994px; width: 981px; height: 206px; background: var(--brand-blue); color: var(--paper); }
  .footer-lip { position: absolute; left: 22px; top: 0; width: 935px; height: 25px; background: var(--paper); }
  .footer-heading { position: absolute; top: 53px; font-family: "Raleway", sans-serif; font-weight: 300; font-size: 22px; letter-spacing: -.6px; }
  .footer-links { position: absolute; font-family: Arial, sans-serif; font-weight: 700; font-size: 12px; line-height: 18px; }
  .social { position: absolute; display: flex; align-items: center; gap: 8px; font-family: Arial, sans-serif; font-weight: 700; font-size: 12px; }
  .social i { width: 18px; height: 18px; border-radius: 50%; background: rgba(255,255,255,.85); display: block; }
  .contact-lines { position: absolute; left: 524px; top: 87px; font-family: Arial, sans-serif; font-size: 12px; line-height: 14px; }
  .contact-phone { position: absolute; left: 522px; top: 118px; display: flex; align-items: center; gap: 6px; font-family: "Yanone Kaffeesatz", sans-serif; font-weight: 400; font-size: 22px; }
  .seal { position: absolute; left: 808px; top: 52px; width: 146px; height: 84px; border-radius: 8px; background: var(--seal-fill); }
  .footer-rule { position: absolute; left: 0; top: 167px; width: 981px; height: 1px; background: rgba(255,255,255,.45); }
  .copyright { position: absolute; left: 23px; top: 181px; font-family: Arial, sans-serif; font-size: 12px; }
</style>
</head>
<body>
  <div class="top-band"></div>

  <header>
    <a href="#" aria-label="The Morrow Tally home">
      <span class="brand-dot"></span>
      <span class="brand-name">THE MORROW TALLY</span>
      <span class="brand-tagline">PATIENT EXPERIENCE DATA COLLECTION &amp; REPORTING</span>
    </a>
    <nav class="main-nav">
      <a href="#">HOME</a>
      <a href="#">CONTACT US</a>
    </nav>
  </header>

  <section class="hero">
    <div class="slide-dots"><span class="is-active"></span><span></span><span></span><span></span><span></span></div>
    <div class="hero-device" role="img" aria-label="Two tablet PCs showing survey reporting bar and line charts"></div>
    <p class="hero-text">The Morrow Tally captures patient, nurse, doctor, employee and visitor satisfaction information in real time quickly and easily on a tablet PC.</p>
  </section>

  <section class="features">
    <div class="feature" style="left:48px">
      <div class="feature-icon" style="margin-left:82px">
        <svg width="40" height="30" viewBox="0 0 40 30" fill="none" stroke="#fff" stroke-width="3"><path d="M2 2v26h36"/><path d="M10 24V14M17 24V10M24 24V12M31 24V6"/></svg>
      </div>
      <h3 class="feature-title" style="margin-left:27px">Real-Time Reporting</h3>
      <p class="feature-text">Percentile Ranking, Return Rates, Top Box Responses, Positive and Negative Trending</p>
      <a class="feature-more" href="#">read more +</a>
    </div>
    <div class="feature" style="left:367px">
      <div class="feature-icon" style="margin-left:83px">
        <svg width="34" height="36" viewBox="0 0 34 36" fill="none" stroke="#fff" stroke-width="3"><rect x="2" y="2" width="22" height="32"/><path d="M7 9h12M7 15h12M7 21h12M7 27h12"/><path d="M30 4v24l-2 5-2-5V4z" fill="#fff"/></svg>
      </div>
      <h3 class="feature-title" style="margin-left:60px">Survey Tools</h3>
      <p class="feature-text">Full Custom Survey Creation, QVRN Banked Surveys and Questions, Custom Question</p>
      <a class="feature-more" href="#">read more +</a>
    </div>
    <div class="feature" style="left:691px">
      <div class="feature-icon" style="margin-left:80px">
        <svg width="40" height="30" viewBox="0 0 40 30" fill="none" stroke="#fff" stroke-width="3"><rect x="7" y="2" width="26" height="19"/><path d="M1 27h38l-4-5H5z" fill="#fff"/><path d="M18 9l4 4" stroke-width="2"/></svg>
      </div>
      <h3 class="feature-title" style="margin-left:14px">On-Site Administration</h3>
      <p class="feature-text" style="width:215px">Full QVRN Application Admin Access, Assign Account Users and Roles</p>
      <a class="feature-more" href="#">read more +</a>
    </div>
  </section>

  <div class="divider"></div>

  <section class="video">
    <div class="video-frame" role="img" aria-label="Video still of a smiling healthcare team in white coats"></div>
    <div class="video-actions">
      <span><svg width="14" height="12" viewBox="0 0 14 12"><path d="M7 12L1 6a3.3 3.3 0 016-4 3.3 3.3 0 016 4z" fill="#fff"/></svg></span>
      <span><svg width="14" height="14" viewBox="0 0 14 14" fill="none" stroke="#fff" stroke-width="1.6"><circle cx="7" cy="7" r="6"/><path d="M7 3v4l3 2"/></svg></span>
      <span><svg width="14" height="14" viewBox="0 0 14 14"><path d="M1 6l12-5-5 12-2-5z" fill="#fff"/></svg></span>
    </div>
    <div class="video-controls">
      <svg width="14" height="14" viewBox="0 0 14 14"><rect x="2" y="1" width="3" height="12" fill="#fff"/><rect x="9" y="1" width="3" height="12" fill="#fff"/></svg>
      <div class="video-track"></div>
    </div>
  </section>

  <section class="pricing">
    <h2 class="pricing-title">YOU WON'T BELIEVE OUR PRICING</h2>
    <div class="pricing-field" style="top:61px">Name</div>
    <div class="pricing-field" style="top:93px">Email</div>
    <div class="pricing-field" style="top:125px">Phone</div>
    <div class="pricing-field" style="top:157px">Company</div>
    <a class="pricing-submit" href="#">SEE PRICING</a>
  </section>

  <footer class="site-footer">
    <div class="footer-lip"></div>

    <h4 class="footer-heading" style="left:23px">NAVIGATION</h4>
    <div class="footer-links" style="left:24px;top:86px"><a href="#">Home</a><br><a href="#">Contact Us</a></div>

    <h4 class="footer-heading" style="left:248px">FOLLOW US</h4>
    <a class="social" href="#" style="left:247px;top:87px"><i></i>Chirper</a>
    <a class="social" href="#" style="left:247px;top:109px"><i></i>Facenote</a>
    <a class="social" href="#" style="left:352px;top:87px"><i></i>Orbit +</a>
    <a class="social" href="#" style="left:352px;top:109px"><i></i>Linkwell</a>

    <h4 class="footer-heading" style="left:523px">CONTACT US</h4>
    <p class="contact-lines">QVRNovation, Mobile Office 1<br>Alderbrook Pennsylvania</p>
    <p class="contact-phone">
      <svg width="16" height="16" viewBox="0 0 16 16" fill="none" stroke="#fff" stroke-width="1.3"><circle cx="8" cy="8" r="7"/><path d="M5.5 4.5l1.5 1.5-1 1a5 5 0 003 3l1-1 1.5 1.5-1 1c-3 0-6-3-6-6z" fill="#fff" stroke="none"/></svg>
      707-555-0142
    </p>

    <a class="seal" href="http://www.fernlattice.example/members/showseal/XyZ4Mw==/QmFzZWxpbmU=/" aria-label="Fernlattice Stewardship Accord platinum seal"></a>

    <div class="footer-rule"></div>
    <p class="copyright">© Copyright The Morrow Tally 2014. All Rights Reserved.</p>
  </footer>
</body>
</html>
```